Flyer-Design für Hundeschule
Zielgruppe
Ich habe eine Hundeschule, seit 11 Jahren, die sich gerade neu aufstellt. Meine Zielgruppe sind junge bis mittel alte Hundemenschen die ihren Hund erziehen möchten und gerne auch ihr Freizeit mit ihm verbringen.
Aufgabenstellung
Ich möchte gerne ein Design was Neukunden anspricht.
Gerne auch, was man sich an den Kühlschrank hängt, weil es so schön ist ;-)
Ich habe sehr viele Fotos vom Profi und kann immer nachliefern, falls deiner Meinung nach etwas nicht ganz passt.
Das Logo habe ich in allen möglichen Dateiformen. Kann ich auch gerne nachliefern.
Vielleicht ist es auch zu viel Text?
Ich bin für alles offen :-)
Die Flyer möchte ich dann bei papier-schnell-fix.de bestellen.
Ich freue mich auf deinen Vorschlag!

```html
<!DOCTYPE html>
<html lang="de">
<head>
<meta charset="utf-8">
<title>PfotenPartner – Flyer</title>
<link href="https://fonts.googleapis.com/css2?family=Open+Sans:wght@400;600;700;800&display=swap" rel="stylesheet">
<style>
  :root{
    --bg:#e3e3e3;
    --paper:#f7f7f5;
    --red:#c4432a;
    --brown:#6b3a2e;
    --ink:#4a4a4a;
    --white:#ffffff;
  }
  *{box-sizing:border-box;margin:0;padding:0}
  html,body{width:1200px;height:1054px;overflow:hidden;background:var(--bg);font-family:"Open Sans",sans-serif;color:var(--ink)}
  .spread{position:absolute;left:40px;width:1120px;height:480px;display:flex;box-shadow:0 6px 18px rgba(0,0,0,.18)}
  .spread--outer{top:30px}
  .spread--inner{top:544px}
  .panel{position:relative;width:560px;height:480px;background:var(--paper);overflow:hidden}
  .panel + .panel{border-left:1px solid #e0e0dc}

  /* outer back */
  .about{position:absolute;top:38px;left:150px;right:50px;text-align:center;font-size:13px;line-height:1.55}
  .about p{margin-bottom:8px}
  .signature{margin-top:6px;font-size:22px;font-weight:600;color:var(--red)}
  .chevrons{position:absolute;color:var(--red);font-weight:800;font-size:26px;letter-spacing:-4px;line-height:1}
  .mascot{position:absolute;left:30px;top:200px;width:110px;height:150px;border-radius:12px;background:linear-gradient(180deg,#efe9e6,#e2d6d1)}
  .band{position:absolute;left:0;right:0;bottom:0;background:var(--red);color:var(--white)}
  .band--back{height:124px;padding:26px 30px 0}
  .url{font-size:22px;font-weight:800;letter-spacing:-.2px;white-space:nowrap;line-height:1.3}
  .contact{margin-top:10px;font-size:10.5px;line-height:1.5}

  /* outer front */
  .band--front{height:220px}
  .brand{position:absolute;top:40px;left:120px;display:flex;align-items:center;gap:14px}
  .brand-dot{width:26px;height:26px;border-radius:50%;background:var(--red)}
  .brand-name{font-size:46px;font-weight:600;color:var(--red);letter-spacing:-.5px}
  .brand-rule{position:absolute;top:104px;left:160px;width:340px;height:2px;background:var(--red)}
  .tagline{position:absolute;top:114px;left:200px;font-size:17px;font-weight:700;color:var(--brown)}
  .photo{position:absolute;border-radius:50%;border:4px solid var(--white);box-shadow:0 3px 8px rgba(0,0,0,.25)}
  .photo--agility{left:36px;top:190px;width:180px;height:180px;background:radial-gradient(circle at 40% 40%,#9bb176,#5f7a45)}
  .photo--boxer{left:232px;top:226px;width:140px;height:140px;background:radial-gradient(circle at 50% 45%,#8fa06a,#4f5c3a)}
  .photo--bulldog{left:366px;top:150px;width:178px;height:178px;background:radial-gradient(circle at 45% 50%,#d9cfc6,#f1efec)}

  /* inner */
  .strip{position:absolute;left:0;right:0;bottom:0;height:16px;background:var(--red)}
  .copy{position:absolute;font-size:10.5px;line-height:1.45}
  .copy h3{font-size:11.5px;font-weight:700;color:var(--red);margin-top:6px}
  .copy ul{list-style:none;padding-left:12px}
  .copy li{margin-top:3px}
  .copy li::before{content:"•";margin-left:-10px;margin-right:5px}
  .copy b{color:#333}
  .copy i{color:#666}
  .copy .sub{padding-left:10px}
  .cta{font-weight:700;color:#333;margin-top:6px}
  .cta span{color:var(--red)}
  .photo--aussie{left:26px;top:160px;width:150px;height:150px;background:radial-gradient(circle at 50% 45%,#b49a86,#6e8ea0)}
  .intro{left:26px;top:24px;right:26px}
  .groups{left:196px;top:126px;right:22px}
  .workshops{left:26px;top:376px;right:26px}
  .col-a{left:26px;top:24px;width:250px}
  .col-b{left:292px;top:24px;width:246px}
  .mini-mascot{position:absolute;right:26px;bottom:30px;width:46px;height:46px;border-radius:8px;background:#ece4e0}
</style>
</head>
<body>

<section class="spread spread--outer">
  <article class="panel panel--back">
    <div class="about">
      <p>Mein Name ist Marlene Voigt, geb. 1986 in Halle.<br>Meine Leben teile ich mit meinem Mann, unserer Tochter und unseren vier Hunden und vier Katzen im schönen Birkenfeld. Seit 2009 bin ich Hundetrainerin aus Leidenschaft.</p>
      <p>Ich setze alles daran, dass Mensch und Hund durch meine Hilfe (wieder) ein Team werden.</p>
      <p>Ich freue mich auf dich und deine Fellnase(n)!<br>Liebe Grüße und hab eine gute Zeit,</p>
      <div class="signature">Marlene Voigt</div>
    </div>
    <div class="chevrons" style="left:34px;top:166px">»</div>
    <div class="chevrons" style="right:18px;top:112px">«</div>
    <div class="mascot" role="img" aria-label="Gezeichneter Hund als Maskottchen"></div>
    <div class="band band--back">
      <div class="url">www.hundetraining-pfotenpartner.de</div>
      <div class="contact">| Hundetraining PfotenPartner (ehemals Hundeschule Brandt) | Marlene Voigt | Lindenweg 7 | 06199 Wiesenau |<br>Mail: kontakt@hundetraining-pfotenpartner.de | Telefon/WhatsApp: 0170-000 124 56</div>
    </div>
  </article>

  <article class="panel panel--front">
    <div class="band band--front"></div>
    <div class="brand"><span class="brand-dot"></span><span class="brand-name">PfotenPartner</span></div>
    <div class="brand-rule"></div>
    <div class="tagline">Hundetraining für jede Schnauze</div>
    <div class="photo photo--agility" role="img" aria-label="Foto: Familie beim Agility-Training mit Hund im Park"></div>
    <div class="photo photo--boxer" role="img" aria-label="Foto: Hund mit Geschirr auf dem Trainingsplatz"></div>
    <div class="photo photo--bulldog" role="img" aria-label="Foto: Bulldogge gibt Pfötchen"></div>
  </article>
</section>

<section class="spread spread--inner">
  <article class="panel panel--inside-left">
    <div class="copy intro">
      <h3>Exklusives Einzeltraining oder doch gemeinsam in einer Hundegruppe lernen?</h3>
      <p>Ich biete dir eine individuelle Lösung.</p>
      <h3>Training in der Gruppe:</h3>
      <p>Gemeinsam lernen macht Spaß und fördert das Sozialverhalten deines Hundes.<br>Alle Kurse finden in 06199 Wiesenau OT Birkenfeld statt.</p>
    </div>
    <div class="photo photo--aussie" role="img" aria-label="Foto: Hund springt durch flaches Wasser"></div>
    <div class="copy groups">
      <ul>
        <li><b>Welpenkurs:</b> Wir legen gemeinsam den optimalen Grundstein für einen sozialen und ruhigen Hund. – Anmeldung bis zur 14. Lebenswoche, Einstieg jederzeit möglich, Dauer 8 Wochen, Kursgebühr 120 € –</li>
        <li><b>Junghundkurs:</b> Zusammenwachsen und aus dem jungen Wilden einen tollen Begleiter machen. – Anmeldung ab dem 4.–10. Monat, Dauer 12 Wochen, Kursgebühr 180 € –</li>
        <li><b>Benimm dich! – Kurs</b> – die vier Säulen des guten Benehmens in Perfektion.
          <div class="sub">· Modul 1: Sicherer Rückruf<br>· Modul 2: Entspanntes Gehen an der Leine<br>· Modul 3: Führen und Folgen<br>· Modul 4: Sitz-Platz-Bleib in Perfektion</div>
          – Anmeldung ab dem 10. Lebensmonat, je Modul 60 €, alle Module 220 € –</li>
      </ul>
    </div>
    <div class="copy workshops">
      <p><b>Workshops:</b> Manchmal hat man nur dieses eine, ganz spezielle Thema mit seinem Hund. Dann sind meine Workshops genau das Richtige. Immer wieder gibt es neue Themen, wie zum Beispiel „Die andere Art der Leinenführung“ oder „Der perfekte Rückruf“. Wir trainieren hier in kleinen Gruppen, um dein Ziel zu erreichen.</p>
    </div>
    <div class="strip"></div>
  </article>

  <article class="panel panel--inside-right">
    <div class="copy col-a">
      <h3>Lust auf Abenteuer und Spaß? Verbringe Zeit mit deinem Hund in meinen Beschäftigungskursen:</h3>
      <ul>
        <li><b>Crossdogging:</b> Du und dein Hund stellen sich wöchentlich neuen spannenden Aufgaben. Hier lernst du auch in Stresssituationen ruhig zu bleiben.</li>
        <li><b>Rally Obedience:</b> Geschicklichkeit und Gehorsam gepaart mit jeder Menge Spaß.</li>
        <li><b>Longieren:</b> Distanz schafft Nähe! Du arbeitest mit deinem Hund über die Distanz am Longierkreis. Ein toller Sport für den Aufbau einer harmonischen Bindung und Beziehung.</li>
      </ul>
      <p class="cta">» Sichere dir jetzt deinen Platz im Kurs oder Workshop unter: <span>www.hundetraining-pfotenpartner.de</span> «</p>
      <h3>Exklusives Einzeltraining</h3>
      <p>Im Einzeltraining liegt mein ganze Aufmerksamkeit nur bei dir und deinem Hund. Die Trainings finden je nach Art bei dir Zuhause oder in Wiesenau OT Birkenfeld statt.</p>
      <ul>
        <li><b>Problemhundtherapie:</b> Dein Hund kann nicht alleine bleiben, zeigt Aggressionen in jeglicher Ausprägung oder ist ein ängstlicher Hund? Dann bist du bei mir genau richtig. Zusammen suchen wir nach der Ursache des Verhaltens.</li>
      </ul>
    </div>
    <div class="copy col-b">
      <p>Zusammen arbeiten wir uns Schritt für Schritt aus dem Problemverhalten heraus, hin zu einer harmonischen Mensch-Hund-Beziehung. <i>(Training vorrangig bei dir Zuhause)</i></p>
      <ul>
        <li><b>Grunderziehung für Hunde ab 6 Monaten:</b> Ich zeige dir, wie du deinen Hund zu einem perfekten Begleiter machen kannst. Egal ob du ihn gerade aus dem Tierheim adoptiert, von privat übernommen hast oder er schon länger bei dir ist. Die kleinen Probleme des Alltags (Leineziehen, Anspringen o.ä.) werden wir schnell lösen. Es ist nie zu spät für eine tolle Mensch-Hund-Beziehung. <i>(Training vorrangig in Wiesenau)</i></li>
        <li><b>Welpenerziehung:</b> Ich zeige dir, wie du eine gute Basis schaffst, in der sich dein Welpe sicher fühlen kann. Dabei spielt gute Sozialisation natürlich eine große Rolle. All das wirst du im Training zusammen mit deinem Hund lernen. <i>(Training vorrangig in Wiesenau)</i></li>
      </ul>
      <p class="cta">» Buche jetzt dein exklusives Einzeltraining unter: <span>www.hundetraining-pfotenpartner.de</span> «</p>
    </div>
    <div class="mini-mascot" role="img" aria-label="Kleiner gezeichneter Hund"></div>
    <div class="strip"></div>
  </article>
</section>

</body>
</html>
```